Dyslexia Assessment Business card design

we need a business card design for a new company based in New Hampshire called Maple Path Learning of NH. We provide dyslexia assessment and consultation
Updates

Can you please add my degrees/certifications Carla Whitmore MA, MEd NH Certified Specialist in the Assessment of Intellectual Functioning Reading and Writing Specialist Learning Disabilities Specialist

I am interested in also creating a web page. If you have experience with webpages that may be useful. I have the domains but am waiting the name of the business to be cleared by the state. I expect this to take place within the month.

I think listing all the certifications is too much. Please just add Carla Whitmore MA, MEd, SAIF

Target Market(s)

parents of kids with dyslexia

Industry/Entity Type

Business

Contact Information for Business Card

Maple Path Learning of NH
Carla Whitmore - Dyslexia Diagnostician/Consultant
42 Tilbury Lane Londonderry, NH 03071
Phone (603)284-7105
WWW.MaplePathLearningofNH-example.com
MaplePathLearningofNH@mailbox-example.com

Requirements
Nice to have
• can have 2 sides not essential though

maybe "dyslexia" in the background spelled wrong or letters backward

```html
<!DOCTYPE html>
<html lang="en">
<head>
<meta charset="utf-8">
<title>Maple Path Learning of NH – Business Card</title>
<link href="https://fonts.googleapis.com/css2?family=Questrial&display=swap" rel="stylesheet">
<style>
  :root {
    --ink: #1b3585;
    --sky: #d5eefa;
    --sky-soft: #e6f5fc;
    --paper: #ffffff;
    --shadow: #a9abae;
  }
  html, body {
    margin: 0;
    padding: 0;
    width: 1200px;
    height: 1000px;
    overflow: hidden;
    background: var(--paper);
  }
  .stage {
    position: relative;
    width: 1200px;
    height: 1000px;
    font-family: "Questrial", "Century Gothic", sans-serif;
    color: var(--ink);
  }
  .card {
    position: absolute;
    left: 249px;
    top: 207px;
    width: 689px;
    height: 403px;
    background: var(--sky);
    box-shadow: 9px 9px 6px var(--shadow);
    overflow: hidden;
  }
  .card-backdrop {
    position: absolute;
    inset: 0;
    background: linear-gradient(125deg, var(--sky) 0%, var(--sky) 45%, var(--sky-soft) 70%, var(--paper) 100%);
  }
  .card-text {
    position: absolute;
    margin: 0;
    white-space: nowrap;
    line-height: 1;
    font-weight: 400;
  }
  .brand-mark {
    left: 24px;
    top: 36px;
    font-size: 42px;
    line-height: 1.05;
  }
  .company-name {
    left: 210px;
    top: 46px;
    font-size: 31px;
  }
  .person-name {
    left: 209px;
    top: 120px;
    font-size: 37px;
  }
  .credentials {
    font-size: 22px;
    margin-left: 14px;
    word-spacing: 4px;
  }
  .job-title {
    left: 209px;
    top: 168px;
    font-size: 27.5px;
  }
  .address {
    left: 90px;
    top: 241px;
    font-size: 23.5px;
  }
  .contact-list {
    position: absolute;
    left: 90px;
    top: 278px;
    margin: 0;
    display: grid;
    grid-template-columns: 76px auto;
    row-gap: 6px;
    align-items: baseline;
  }
  .contact-label {
    margin: 0;
    font-size: 19px;
  }
  .contact-value {
    margin: 0;
    font-size: 23px;
    line-height: 1.05;
    white-space: nowrap;
  }
</style>
</head>
<body>
<div class="stage">
  <section class="card">
    <div class="card-backdrop" role="img" aria-label="Soft light-blue background with flowing curved bands"></div>

    <p class="card-text brand-mark">Maple<br>Path</p>

    <h1 class="card-text company-name">Maple Path Learning of NH</h1>
    <p class="card-text person-name">Carla Whitmore<span class="credentials">MA&nbsp;&nbsp;MEd&nbsp;&nbsp;SAIF</span></p>
    <p class="card-text job-title">Dyslexia Diagnostician/Consultant</p>

    <p class="card-text address">42 Tilbury Lane, Londonderry, NH 03071</p>
    <dl class="contact-list">
      <dt class="contact-label">T:</dt>
      <dd class="contact-value">(603)284-7105</dd>
      <dt class="contact-label">W:</dt>
      <dd class="contact-value">WWW.MaplePathLearningofNH-example.com</dd>
      <dt class="contact-label">E:</dt>
      <dd class="contact-value">MaplePathLearningofNH@mailbox-example.com</dd>
    </dl>
  </section>
</div>
</body>
</html>
```